Stylish, Masculine Design - Men's Clothing

Granary Coat Mart is a 14,000 square foot warehouse outlet store open to the public since 2005. 50+ brands. Well-known designer brand names and private labels. 30-80% off retail everyday. Lowest prices guaranteed. Average suit price $150. Average shirt price $20. One-stop shop shopping. Men's suits, tuxedos, tuxedo rentals, dress shirts, ties, dress shoes, boy's suits and tuxedos, clergy robes, clergy shirts, cologne, loungewear. Slim fits (Prom Dance), business styles, "church" fashion, security-related uniform. Alterations done by expert tailors on premises for an extra charge.
The final design for both business card and logo should portray stylishness and masculinity.
Updates
We will be changing our name. Details below.New name: Warehouse Suit & TuxFormer name: Granary Coat Mart Added Monday, December 26, 2016
Target Market(s)
Gender: 80% Male, 15% Female, 5% Transgender
Location: 80% 10 Mile Radius, 20% >10 Mile Radius
Age: 17-18 (Primarily prom), 18-35 (Primarily Interviews and Weddings), 36-70 (primarily Church and events)
Race: African-American 50%, Latino-American 20%, White 15%, 10% Asian 5% Other
Religions: Christian 50%, 20% Catholic, 10% Mormon, 20% Other/None
Occupation: Local government 40%, Large corporation employee 20%, Small business employee 10%, Small business owner 10%, 20% Unemployed (high school, college)
Education: High School or equivalent 40%, College 30%, Some College 20%, Masters/Doctors 10%
Industry/Entity Type
Retail
Contact Information for Business Card
Name: Peter Olund
Title: Sales Associate
Address: 418 E. Mirabeth Ave. Larkfield, OR 97390
Phone Number: 541.555.0182
Slogan: Broad Selection. Honest Prices, Attentive Tailoring
www.granarycoatmart.example
Logo Text
GCM (Acronym for Granary Coat Mart) or Image
Requirements
Must have
- Easy to read
- Visually appealing

```html
<!DOCTYPE html>
<html lang="en">
<head>
<meta charset="utf-8">
<title>Granary Coat Mart – Business Card</title>
<link rel="stylesheet" href="https://fonts.googleapis.com/css2?family=Source+Sans+3:wght@400;600;700&display=swap">
<style>
  :root {
    --backdrop: #e9e6e2;
    --card-white: #ffffff;
    --ink-black: #0b0b0b;
    --brand-red: #e3191f;
    --text-white: #ffffff;
  }
  * { box-sizing: border-box; margin: 0; padding: 0; }
  html, body {
    width: 1200px;
    height: 987px;
    overflow: hidden;
    background: var(--backdrop);
    font-family: "Source Sans 3", sans-serif;
  }
  .stage {
    position: relative;
    width: 1200px;
    height: 987px;
  }
  .card {
    position: absolute;
    left: 293px;
    width: 615px;
    height: 351px;
    box-shadow: 0 3px 10px rgba(0,0,0,0.25);
    overflow: hidden;
  }
  .card--front { top: 130px; background: var(--card-white); }
  .card--back  { top: 505px; background: var(--ink-black); }

  .brand-name {
    position: absolute;
    left: 0;
    right: 0;
    text-align: center;
    font-weight: 600;
    font-size: 42px;
    line-height: 44px;
    letter-spacing: 3px;
    text-transform: uppercase;
  }
  .card--front .brand-name { top: 62px; color: var(--ink-black); }
  .card--back .brand-name  { top: 120px; color: var(--text-white); }

  .info-band {
    position: absolute;
    top: 221px;
    height: 100px;
    padding: 18px 20px 0 40px;
  }
  .info-band--person {
    left: 0;
    width: 307px;
    background: var(--ink-black);
    color: var(--text-white);
  }
  .info-band--contact {
    left: 309px;
    width: 306px;
    background: var(--brand-red);
    color: var(--text-white);
    text-align: right;
    padding: 18px 38px 0 20px;
  }
  .person-name {
    color: var(--brand-red);
    font-weight: 600;
    font-size: 21px;
    line-height: 24px;
    text-transform: uppercase;
  }
  .person-title, .person-web, .contact-line {
    font-size: 16px;
    line-height: 23px;
  }
  .contact-line strong { font-weight: 700; }

  .slogan-strip {
    position: absolute;
    left: 0;
    right: 0;
    top: 302px;
    height: 27px;
    background: var(--card-white);
    color: var(--brand-red);
    font-size: 16px;
    line-height: 27px;
    text-align: center;
  }
</style>
</head>
<body>
<main class="stage">
  <section class="card card--front" aria-label="Business card front">
    <h1 class="brand-name">Granary<br>Coat Mart</h1>
    <div class="info-band info-band--person">
      <p class="person-name">Peter Olund</p>
      <p class="person-title">Sales Associate</p>
      <p class="person-web">www.granarycoatmart.example</p>
    </div>
    <div class="info-band info-band--contact">
      <p class="contact-line">418 E. Mirabeth Ave.</p>
      <p class="contact-line">Larkfield, OR 97390</p>
      <p class="contact-line"><strong>Phone:</strong> 541.555.0182</p>
    </div>
  </section>

  <section class="card card--back" aria-label="Business card back">
    <h2 class="brand-name">Granary<br>Coat Mart</h2>
    <p class="slogan-strip">Broad Selection. Honest Prices, Attentive Tailoring</p>
  </section>
</main>
</body>
</html>
```